GDFH Business Card

Looking for a business card design to incorporate our branding. We want to only use the colors listing in the Branding Package (attached).
Updates

Target Market(s)

People who need their phone or device fixed.

Industry/Entity Type

Electronics

Contact Information for Business Card

Please use:

Gadget Fix Haven LLC
4870 S Ridgecrest Pkwy
Suite 318
San Antonio, TX 78291

Wendell Thorsby, Store Manager

(210) 555-0147

Requirements
Must have
• Must include the colors that are contained within the Branding Package PDF file.

```html
<!DOCTYPE html>
<html lang="en">
<head>
<meta charset="utf-8">
<title>GDFH Business Card</title>
<link rel="stylesheet" href="https://fonts.googleapis.com/css2?family=Lato:wght@400;700&display=swap">
<style>
  :root {
    --bg: #ececec;
    --card: #111111;
    --orange: #e8581c;
    --white: #f4f4f4;
  }
  * { box-sizing: border-box; margin: 0; padding: 0; }
  html, body { width: 1200px; height: 1200px; overflow: hidden; }
  body {
    background: var(--bg);
    font-family: "Lato", Arial, sans-serif;
    position: relative;
  }
  .card {
    position: absolute;
    left: 250px;
    width: 700px;
    height: 400px;
    background: var(--card);
    border-bottom: 4px solid var(--orange);
    border-left: 2px solid var(--orange);
    box-shadow: 0 8px 22px rgba(0,0,0,0.18);
    overflow: hidden;
  }
  .card--front { top: 120px; }
  .card--back { top: 680px; }

  .brand {
    position: absolute;
    display: flex;
    align-items: center;
    gap: 14px;
    color: var(--orange);
    font-weight: 700;
    white-space: nowrap;
  }
  .brand__square {
    display: block;
    background: var(--orange);
    border-radius: 6px;
  }
  .card--front .brand {
    left: 50%; top: 50%;
    transform: translate(-50%, -50%);
    font-size: 40px;
  }
  .card--front .brand__square { width: 46px; height: 46px; }
  .card--back .brand {
    right: 48px; top: 48px;
    font-size: 28px;
  }
  .card--back .brand__square { width: 34px; height: 34px; border-radius: 5px; }

  .rule-vertical {
    position: absolute;
    left: 56px; top: 40px; bottom: 20px;
    width: 2px;
    background: var(--orange);
  }
  .contact {
    position: absolute;
    left: 90px; bottom: 60px;
    color: var(--white);
  }
  .contact__name {
    color: var(--orange);
    font-size: 24px;
    font-weight: 700;
    text-transform: uppercase;
    letter-spacing: 0.5px;
    padding-bottom: 6px;
    border-bottom: 2px solid var(--orange);
    width: 260px;
  }
  .contact__title { font-size: 17px; margin-top: 6px; }
  .contact__row {
    display: flex;
    align-items: flex-start;
    gap: 12px;
    font-size: 16px;
    line-height: 1.35;
    margin-top: 18px;
  }
  .contact__icon { width: 16px; height: 16px; flex: none; margin-top: 2px; }
</style>
</head>
<body>
  <section class="card card--front" aria-label="Business card front">
    <div class="brand"><span class="brand__square"></span>Gadget Fix Haven</div>
  </section>

  <section class="card card--back" aria-label="Business card back">
    <div class="brand"><span class="brand__square"></span>Gadget Fix Haven</div>
    <span class="rule-vertical"></span>
    <div class="contact">
      <p class="contact__name">Wendell Thorsby</p>
      <p class="contact__title">Store Manager</p>
      <div class="contact__row">
        <svg class="contact__icon" viewBox="0 0 16 16" aria-hidden="true">
          <rect width="16" height="16" rx="2" fill="var(--orange)"/>
          <path d="M8 3a3.2 3.2 0 0 0-3.2 3.2C4.8 8.6 8 13 8 13s3.2-4.4 3.2-6.8A3.2 3.2 0 0 0 8 3zm0 4.4a1.2 1.2 0 1 1 0-2.4 1.2 1.2 0 0 1 0 2.4z" fill="#fff"/>
        </svg>
        <p>4870 S Ridgecrest Pkwy, Suite 318<br>San Antonio, TX 78291</p>
      </div>
      <div class="contact__row">
        <svg class="contact__icon" viewBox="0 0 16 16" aria-hidden="true">
          <rect width="16" height="16" rx="2" fill="var(--orange)"/>
          <path d="M5.2 3.5l1.6 2.2-.9 1.1c.6 1.3 1.6 2.3 2.9 2.9l1.1-.9 2.2 1.6-.8 1.8c-4.3-.3-7.6-3.6-7.9-7.9z" fill="#fff"/>
        </svg>
        <p>(210) 555-0147</p>
      </div>
    </div>
  </section>
</body>
</html>
```